"Brightly Bold Sisters" book

I am self-publishing a legal guide for women, which will give them information about their rights and how to navigate the legal world in an easy-to-read style. I'd like to see a design using the colours in the logo I've also had designed for the brand by the same name. Then I can provide the winner my photo and a blurb for the back cover. I am the author: Melda Strovik.

Font styles to use
Serif

Requirements
Must have
• Casual but trustworthy feel. Not too formal - it's not a legal text book.
• Back cover must have my photo, a space for the blurb, and a space for the barcode
Nice to have
• Abstract - not my photo on the front, and not a bunch of smiling women either.

```html
<!DOCTYPE html>
<html lang="en">
<head>
<meta charset="utf-8">
<title>Legal Guide for Women – Book Cover</title>
<link rel="stylesheet" href="https://fonts.googleapis.com/css2?family=Cinzel:wght@700&family=Source+Sans+3:wght@400&display=swap">
<style>
  :root {
    --page: #ffffff;
    --ink: #3a3328;
    --edge: #1a1a1a;
    --mustard: #c2953a;
    --caramel: #b5844f;
    --honey: #f0b454;
    --taupe: #746a5e;
    --light: #ffffff;
  }
  html, body {
    margin: 0;
    width: 1200px;
    height: 1200px;
    overflow: hidden;
    background: var(--page);
  }
  .canvas {
    position: relative;
    width: 1200px;
    height: 1200px;
  }
  .book-cover {
    position: absolute;
    left: 402px;
    top: 304px;
    width: 395px;
    height: 591px;
  }
  .cover-title {
    font-family: "Cinzel", "Times New Roman", serif;
    font-weight: 700;
    font-size: 48px;
    fill: var(--ink);
  }
  .cover-author {
    font-family: "Source Sans 3", "Helvetica Neue", sans-serif;
    font-size: 17px;
    fill: var(--light);
  }
  .imprint-name {
    font-family: "Source Sans 3", "Helvetica Neue", sans-serif;
    font-size: 14px;
    fill: var(--light);
  }
</style>
</head>
<body>
<main class="canvas">
  <svg class="book-cover" viewBox="0 0 395 591" xmlns="http://www.w3.org/2000/svg">
    <rect class="cover-base" x="0" y="0" width="395" height="591" fill="var(--page)"/>

    <g class="accent-bar">
      <rect x="0" y="13" width="96" height="18" fill="var(--mustard)"/>
      <rect x="96" y="13" width="100" height="18" fill="var(--caramel)"/>
      <rect x="196" y="13" width="99" height="18" fill="var(--honey)"/>
      <rect x="295" y="13" width="100" height="18" fill="var(--taupe)"/>
    </g>

    <text class="cover-title" x="203" y="80" text-anchor="middle" textLength="322" lengthAdjust="spacingAndGlyphs">LEGAL GUIDE</text>
    <text class="cover-title" x="203" y="128" text-anchor="middle" textLength="305" lengthAdjust="spacingAndGlyphs">FOR WOMEN</text>

    <g class="stripe-panel">
      <rect x="0" y="139" width="100" height="441" fill="var(--taupe)"/>
      <rect x="100" y="139" width="99" height="441" fill="var(--honey)"/>
      <rect x="199" y="139" width="100" height="441" fill="var(--caramel)"/>
      <rect x="299" y="139" width="96" height="441" fill="var(--mustard)"/>
    </g>

    <text class="cover-author" x="368" y="162" text-anchor="end">Melda Strovik</text>

    <rect class="figure-area" role="img" aria-label="Silhouette of a standing woman with hands on hips"
          x="34" y="164" width="134" height="374" rx="20" fill="var(--honey)" opacity="0.55"/>
    <rect class="figure-area" role="img" aria-label="Silhouette of a woman in a business dress carrying a briefcase"
          x="226" y="196" width="148" height="368" rx="20" fill="var(--taupe)" opacity="0.45"/>

    <g class="imprint">
      <circle cx="138" cy="553" r="8" fill="var(--light)"/>
      <text class="imprint-name" x="151" y="558">Brightly Bold Sisters</text>
    </g>

    <line x1="0" y1="0.5" x2="394" y2="0.5" stroke="var(--edge)" stroke-width="1"/>
    <line x1="0.5" y1="0" x2="0.5" y2="591" stroke="var(--edge)" stroke-width="1"/>
  </svg>
</main>
</body>
</html>
```